EPIC, awesome, creative business card needed - get involved!

I'm launching a boutique, exclusive Property Management real estate agency in Sydney early next year.
The name of the agency will be called "Quartz Hill Lane" - it's a play on "chase the silver pebble trail" to wealth. The Quartz Hill Lane signifies wealth through property investment.
My business will offer management of investment properties (ie Property Management).
The difference with Quartz Hill Lane and other agencies is the business will be run by one of Australia's leading property investment experts, and also one of Australia's leading property managers.
It will be exclusively for high net worth properties and individuals, so the business card needs to be extremely sharp, slick and relatively simple.
The information I want on the card is as follows
Nolan Pryce - Director
M: 0412 967 154
P: 9735 6021
E: nolan@quartzhilllane.net.au
W: quartzhilllane.net.au
I'm happy with the red from the logo, black - no yellows or funky colors. I want this to be a super corporate and slick business card to match the high end nature of the business.
Good luck everyone, and please ask questions for clarification.

```html
<!DOCTYPE html>
<html lang="en">
<head>
<meta charset="utf-8">
<title>Quartz Hill Lane — Business Card</title>
<link rel="stylesheet" href="https://fonts.googleapis.com/css2?family=Roboto:wght@400;500;700&display=swap">
<style>
  :root {
    --stage-top: #414143;
    --stage-bottom: #939498;
    --card: #ffffff;
    --brand-red: #c00000;
    --ink: #2b2b28;
    --band: #33312a;
    --band-text: #f4f4f2;
  }
  * { box-sizing: border-box; margin: 0; padding: 0; }
  html, body { width: 1200px; height: 900px; overflow: hidden; }
  body {
    position: relative;
    font-family: "Roboto", Arial, sans-serif;
    background: var(--stage-bottom);
    color: var(--ink);
  }
  .stage-top {
    position: absolute; left: 0; top: 0;
    width: 1200px; height: 368px;
    background: var(--stage-top);
  }
  .card {
    position: absolute;
    width: 420px; height: 240px;
    background: var(--card);
    overflow: hidden;
  }
  .card--combined { left: 390px; top: 64px; }
  .card--front { left: 152px; top: 514px; }
  .card--back { left: 628px; top: 514px; }

  .wordmark {
    position: absolute;
    color: var(--brand-red);
    font-weight: 700;
    font-size: 16px;
    line-height: 18px;
    letter-spacing: 0.5px;
    text-transform: uppercase;
  }
  .card--combined .wordmark { left: 8px; top: 84px; }
  .card--front .wordmark { left: 72px; top: 88px; }
  .card--back .wordmark { left: 282px; top: 88px; }

  .identity { position: absolute; white-space: nowrap; }
  .identity .name { font-size: 19px; line-height: 22px; }
  .identity .role { font-size: 14px; line-height: 17px; }

  .card--combined .identity { left: 89px; top: 101px; }
  .card--combined .identity .name { font-size: 18px; font-weight: 700; }

  .divider {
    position: absolute; left: 195px; top: 80px;
    width: 2px; height: 80px;
    background: var(--brand-red);
  }

  .contact { position: absolute; list-style: none; white-space: nowrap; }
  .card--combined .contact {
    left: 212px; top: 85px;
    font-size: 14.5px; line-height: 17px;
  }

  .band {
    position: absolute; top: 79px;
    height: 80px;
    background: var(--band);
    color: var(--band-text);
  }
  .card--front .band { left: 210px; width: 210px; }
  .card--front .identity { left: 21px; top: 19px; }
  .card--front .identity .name { font-weight: 400; }

  .card--back .band { left: 0; width: 209px; }
  .card--back .contact {
    left: 19px; top: 8px;
    font-size: 12.5px; line-height: 16px;
  }
  .card--back .contact .label { display: inline-block; width: 18px; }
</style>
</head>
<body>
  <div class="stage-top"></div>

  <section class="card card--combined" aria-label="Business card, single-sided layout">
    <div class="wordmark">Quartz<br>Hill<br>Lane</div>
    <div class="identity">
      <p class="name">Nolan Pryce</p>
      <p class="role">Director</p>
    </div>
    <div class="divider"></div>
    <ul class="contact">
      <li>M: 0412 967 154</li>
      <li>P. 9735 6021</li>
      <li>E: nolan@quartzhilllane.net.au</li>
      <li>W: quartzhilllane.net.au</li>
    </ul>
  </section>

  <section class="card card--front" aria-label="Business card front">
    <div class="wordmark">Quartz<br>Hill<br>Lane</div>
    <div class="band">
      <div class="identity">
        <p class="name">Nolan Pryce</p>
        <p class="role">Director</p>
      </div>
    </div>
  </section>

  <section class="card card--back" aria-label="Business card back">
    <div class="band">
      <ul class="contact">
        <li><span class="label">M</span>: 0412 967 154</li>
        <li><span class="label">P</span>: 9735 6021</li>
        <li><span class="label">E</span>: nolan@quartzhilllane.net.au</li>
        <li><span class="label">W</span>: quartzhilllane.net.au</li>
      </ul>
    </div>
    <div class="wordmark">Quartz<br>Hill<br>Lane</div>
  </section>
</body>
</html>
```